Professional Business Cards for Janitorial Company

We are a Janitorial Company that services Commercial Buildings.

Our Logo is included. It can't look silly or cartoonish. Has to look professional.

Information:
Derek Malloy
Operations Manager
619.437.2086
DMalloy@BrightwayFacilityCare.com
www.BrightwayFacilityCare.com

```html
<!DOCTYPE html>
<html lang="en">
<head>
<meta charset="utf-8">
<title>Brightway Facility Care – Business Cards</title>
<link href="https://fonts.googleapis.com/css2?family=Open+Sans:wght@400;600;700&family=Oswald:wght@400;500&display=swap" rel="stylesheet">
<style>
  :root {
    --brand-blue: #26a9e0;
    --brand-blue-light: #4dbde9;
    --card-white: #f7f7f7;
    --band-grey: #dcdcdc;
    --band-grey-dark: #c9c9c9;
    --text-dark: #3c3c3c;
    --text-mid: #555555;
    --backdrop: #e9e9e6;
  }
  * { box-sizing: border-box; margin: 0; padding: 0; }
  html, body { width: 1200px; height: 927px; overflow: hidden; }
  body {
    background: var(--backdrop);
    font-family: "Open Sans", Arial, sans-serif;
    position: relative;
  }
  .card {
    position: absolute;
    width: 540px;
    height: 309px;
    background: var(--card-white);
    box-shadow: 0 8px 24px rgba(0,0,0,0.18);
    overflow: hidden;
  }
  /* Front face */
  .card--front { left: 60px; top: 110px; }
  .front-panel {
    position: absolute;
    inset: 26px 28px;
    background: var(--brand-blue);
    display: flex;
    align-items: center;
    justify-content: center;
    gap: 14px;
  }
  .front-mark {
    width: 34px; height: 34px;
    background: #ffffff;
  }
  .front-name {
    color: #ffffff;
    font-weight: 700;
    font-size: 30px;
    line-height: 1;
    letter-spacing: -0.3px;
  }
  /* Back face */
  .card--back { left: 600px; top: 500px; }
  .corner-band {
    position: absolute;
    right: 0; top: 0;
    width: 70px; height: 30px;
    background: var(--band-grey);
  }
  .holder {
    position: absolute;
    right: 26px; top: 42px;
    text-align: right;
  }
  .holder-name {
    font-family: "Oswald", "Arial Narrow", sans-serif;
    font-weight: 500;
    font-size: 26px;
    color: var(--brand-blue);
    line-height: 1;
    letter-spacing: 0.5px;
  }
  .holder-title {
    font-size: 12px;
    color: var(--text-dark);
    margin-top: 3px;
  }
  .accent-bar {
    position: absolute;
    right: 0; top: 120px;
    width: 235px; height: 24px;
    background: var(--brand-blue);
  }
  .grey-band {
    position: absolute;
    left: 0; top: 190px;
    width: 540px; height: 30px;
    background: var(--band-grey);
  }
  .grey-band-accent {
    position: absolute;
    left: 0; top: 190px;
    width: 38px; height: 30px;
    background: var(--brand-blue-light);
  }
  .back-brand {
    position: absolute;
    left: 60px; top: 148px;
    display: flex;
    align-items: center;
    gap: 10px;
  }
  .back-mark {
    width: 22px; height: 22px;
    background: var(--brand-blue);
  }
  .back-name {
    color: var(--brand-blue);
    font-weight: 700;
    font-size: 22px;
    line-height: 1;
  }
  .contact {
    position: absolute;
    left: 60px; top: 228px;
    list-style: none;
    font-size: 13px;
    line-height: 21px;
    color: var(--text-mid);
  }
</style>
</head>
<body>
  <section class="card card--front" aria-label="Card front">
    <div class="front-panel">
      <span class="front-mark"></span>
      <span class="front-name">Brightway Facility Care</span>
    </div>
  </section>

  <section class="card card--back" aria-label="Card back">
    <div class="corner-band"></div>
    <div class="holder">
      <p class="holder-name">DEREK MALLOY</p>
      <p class="holder-title">Operations Manager</p>
    </div>
    <div class="accent-bar"></div>
    <div class="back-brand">
      <span class="back-mark"></span>
      <span class="back-name">Brightway Facility Care</span>
    </div>
    <div class="grey-band"></div>
    <div class="grey-band-accent"></div>
    <ul class="contact">
      <li>619.437.2086</li>
      <li>DMalloy@BrightwayFacilityCare.com</li>
      <li>www.BrightwayFacilityCare.com</li>
    </ul>
  </section>
</body>
</html>
```